Letterhead and envelope design

Using current logo and colours I would like to have a new design done for a stationary set to be printed.

The new files should include logo, web and email address as well as,mailing address and phone number

Rory Vantosh
Vantosh Building Inc
Box 27 Site 18 RR5
Alderwick NR
T4M 2B7
Cell : 403-555-2917
Email: rory@vantoshbuilding.example
web: vantoshbuilding.example

```html
<!DOCTYPE html>
<html lang="en">
<head>
<meta charset="utf-8">
<title>Vantosh Building – Stationery Set</title>
<link rel="stylesheet" href="https://fonts.googleapis.com/css2?family=Source+Sans+3:wght@400;600;700&display=swap">
<style>
  :root {
    --backdrop: #474747;
    --paper: #ffffff;
    --navy: #141c28;
    --orange: #cf6e2c;
    --text: #3c3c3c;
    --ink: #111111;
    --watermark: #e3e3e8;
    --rule: #222222;
  }
  * { margin: 0; padding: 0; box-sizing: border-box; }
  html, body { width: 960px; height: 1200px; overflow: hidden; }
  body {
    background: var(--backdrop);
    font-family: "Source Sans 3", "Myriad Pro", Arial, sans-serif;
    position: relative;
  }
  .sheet {
    position: absolute;
    background: var(--paper);
    overflow: hidden;
  }
  .sheet__footer-band {
    position: absolute; left: 0; right: 0; bottom: 0;
    height: 15px; background: var(--orange);
  }
  .watermark { position: absolute; z-index: 0; }

  /* brand lockup */
  .brand-band {
    position: absolute; left: 0;
    background: var(--navy);
  }
  .brand-dot {
    position: absolute;
    width: 64px; height: 64px; border-radius: 50%;
    background: var(--navy);
    box-shadow: 0 0 0 4px var(--paper);
  }
  .brand-name {
    position: absolute;
    font-weight: 600; font-size: 13px; line-height: 13px;
    color: var(--navy); letter-spacing: 0.3px; text-transform: uppercase;
  }

  /* letterhead */
  .letterhead { left: 171px; top: 50px; width: 618px; height: 798px; }
  .letterhead .brand-band { top: 25px; width: 90px; height: 61px; }
  .letterhead .brand-dot { left: 71px; top: 24px; }
  .letterhead .brand-name { left: 144px; top: 43px; }
  .letterhead .watermark { left: 160px; top: 272px; }

  .sender-address {
    position: absolute; left: 303px; top: 36px;
    font-size: 9.6px; line-height: 12px; color: var(--ink);
    font-style: normal;
  }
  .sender-address strong { font-weight: 700; }
  .header-divider {
    position: absolute; left: 416px; top: 30px;
    width: 1px; height: 48px; background: var(--rule);
  }
  .contact-list {
    position: absolute; left: 436px; top: 36px;
    list-style: none; font-size: 9.6px; line-height: 12px; color: var(--ink);
  }
  .contact-list li { display: flex; align-items: center; gap: 6px; }
  .contact-list svg { width: 8px; height: 8px; flex: none; }

  .letter-body {
    position: absolute; left: 53px; top: 244px; width: 512px;
    z-index: 1; color: var(--text);
    font-size: 12px; line-height: 14.4px;
  }
  .salutation { margin-bottom: 36px; }
  .letter-body p.para { text-align: justify; margin-bottom: 14.4px; }
  .letter-body p.para--first { text-indent: 36px; }

  /* envelope */
  .envelope { left: 154px; top: 866px; width: 652px; height: 291px; }
  .envelope .brand-band { top: 32px; width: 86px; height: 60px; }
  .envelope .brand-dot { left: 72px; top: 30px; }
  .envelope .brand-name { left: 143px; top: 50px; }
  .envelope .watermark { left: 330px; top: 34px; }
  .return-address {
    position: absolute; left: 26px; top: 222px;
    font-size: 9.6px; line-height: 12.3px; color: var(--ink);
    font-style: normal; z-index: 1;
  }
  .return-address strong { font-weight: 700; }
</style>
</head>
<body>

<section class="sheet letterhead" aria-label="Letterhead">
  <svg class="watermark" width="330" height="330" viewBox="0 0 330 330" aria-hidden="true">
    <circle cx="165" cy="165" r="165" fill="var(--watermark)"/>
  </svg>

  <div class="brand-band"></div>
  <div class="brand-dot"></div>
  <div class="brand-name">Vantosh<br>Building</div>

  <address class="sender-address">
    <strong>Vantosh Building Inc</strong><br>
    Box 27 Site 18 RR5<br>
    Alderwick NR<br>
    T4M 2B7
  </address>
  <div class="header-divider"></div>
  <ul class="contact-list">
    <li>
      <svg viewBox="0 0 8 8" aria-hidden="true"><rect x="1.5" y="0" width="5" height="8" rx="1" fill="var(--orange)"/><rect x="2.5" y="1" width="3" height="5" fill="#fff"/></svg>
      403-555-2917
    </li>
    <li>
      <svg viewBox="0 0 8 8" aria-hidden="true"><circle cx="4" cy="4" r="3.4" fill="none" stroke="var(--orange)" stroke-width="1"/><ellipse cx="4" cy="4" rx="1.4" ry="3.4" fill="none" stroke="var(--orange)" stroke-width="0.8"/><line x1="0.6" y1="4" x2="7.4" y2="4" stroke="var(--orange)" stroke-width="0.8"/></svg>
      rory@vantoshbuilding.example
    </li>
    <li>
      <svg viewBox="0 0 8 8" aria-hidden="true"><rect x="0.5" y="2" width="7" height="5" fill="var(--orange)"/><polyline points="0.5,2 4,4.8 7.5,2" fill="none" stroke="#fff" stroke-width="0.8"/></svg>
      vantoshbuilding.example
    </li>
  </ul>

  <div class="letter-body">
    <p class="salutation">Dear Dr</p>
    <p class="para para--first">Lorem ipsum dolor sit amet, consectetur adipiscing elit. Integer eu odio mattis, pulvinar turpis quis, faucibus nisl. Proin feugiat, erat vitae cursus pharetra, enim est semper ligula, in malesuada orci nisl et diam. Etiam elementum metus ac fringilla vulputate. Etiam mattis ligula sed ante mollis bibendum. Orci varius natoque penatibus et magnis dis parturient montes, nascetur ridiculus mus.</p>
    <p class="para">Ut nibh augue, blandit ac orci ac, rutrum congue enim. Suspendisse gravida vulputate felis, quis interdum orci tincidunt quis. Praesent imperdiet maximus neque. Mauris ut dui enim. Nullam at efficitur elit. Donec ante ipsum, fermentum at lectus vel, blandit vulputate ante. Proin luctus suscipit diam id vestibulum. Morbi malesuada id mauris eget ullamcorper.</p>
    <p class="para">Donec varius orci purus, vitae aliquam libero volutpat id. Integer sed imperdiet libero. Aliquam accumsan, risus sit amet ornare consectetur, turpis felis dictum justo, non rhoncus mauris dui sed velit. Pellentesque habitant morbi tristique senectus et netus et malesuada fames ac turpis egestas. Pellentesque tincidunt vitae ligula nec imperdiet. Donec sed congue enim. Nullam elementum faucibus nulla nec vestibulum. Sed at tempor ligula. In quis vulputate nunc. Integer at gravida lacus, ac tristique risus. Sed at vulputate nulla.</p>
    <p class="para">Praesent blandit nunc eu efficitur commodo. In tempor nisi ex, vel venenatis ante vestibulum a. Duis vestibulum nibh a erat sagittis, nec euismod lorem varius. Nam ultricies turpis sed justo sollicitudin volutpat. Morbi sed mollis eros. Sed quis tortor id enim vehicula porttitor. Curabitur non aliquam ex. Phasellus dignissim fermentum elit, at finibus ligula mattis eget.</p>
  </div>

  <div class="sheet__footer-band"></div>
</section>

<section class="sheet envelope" aria-label="Envelope">
  <svg class="watermark" width="328" height="328" viewBox="0 0 328 328" aria-hidden="true">
    <circle cx="164" cy="164" r="164" fill="var(--watermark)"/>
  </svg>

  <div class="brand-band"></div>
  <div class="brand-dot"></div>
  <div class="brand-name">Vantosh<br>Building</div>

  <address class="return-address">
    <strong>Vantosh Building Inc</strong><br>
    Box 27 Site 18 RR5<br>
    Alderwick NR<br>
    T4M 2B7
  </address>

  <div class="sheet__footer-band"></div>
</section>

</body>
</html>
```